New Zealand Marlborough Sauvignon Blanc wine packaging design

We need packaging design for our new wine brand, Dunmore Hale. The wine is a New Zealand Marlborough Sauvignon Blanc. We would like the packaging will portray elegance and style with an understated label. We are looking for a label that portrays the elegance of the French Riviera. The label should be round or pill shaped.
Updates

Industry/Entity Type

Wine

Font styles to use
Serif
Sans Serif

Requirements
Must have
• The words in order of importance: Dunmore Hale, Sauvignon Blanc, Marlborough, New Zealand. It should be fit to the bottle posted in the links
Nice to have
• a pill shape or circular shape
Should not have
• Illustrations of wine bottles, wine glasses, or grapes

```html
<!DOCTYPE html>
<html lang="en">
<head>
<meta charset="utf-8">
<title>Dunmore Hale — Marlborough Sauvignon Blanc Label</title>
<link href="https://fonts.googleapis.com/css2?family=Old+Standard+TT:wght@700&display=swap" rel="stylesheet">
<style>
  :root {
    --bg: #f1f1f1;
    --forest: #0c3230;
    --olive: #4d5a3a;
    --gold: #e6a93a;
    --gold-deep: #b9801f;
    --paper: #ffffff;
  }
  html, body {
    margin: 0;
    width: 1200px;
    height: 1200px;
    overflow: hidden;
    background: var(--bg);
  }
  .canvas {
    width: 1200px;
    height: 1200px;
    display: flex;
    align-items: center;
    justify-content: center;
  }
  .label { width: 920px; height: 920px; display: block; }
  .label-body { fill: var(--forest); }
  .border-band { fill: none; stroke: var(--olive); stroke-width: 14; }
  .name-ring { fill: var(--paper); }
  .scene-field { stroke: none; }
  .brand-name {
    font-family: "Old Standard TT", Georgia, serif;
    font-weight: 700;
    font-size: 92px;
    fill: var(--gold);
    letter-spacing: 1px;
  }
  .country {
    font-family: "Old Standard TT", Georgia, serif;
    font-weight: 700;
    font-size: 40px;
    fill: var(--paper);
  }
  .detail {
    font-family: "Old Standard TT", Georgia, serif;
    font-weight: 700;
    font-size: 25px;
    fill: var(--forest);
  }
  .star { fill: var(--gold); }
</style>
</head>
<body>
<main class="canvas">
  <svg class="label" viewBox="-375 -375 750 750" xmlns="http://www.w3.org/2000/svg" role="group" aria-label="Dunmore Hale Sauvignon Blanc label">
    <defs>
      <mask id="notch-mask">
        <rect x="-375" y="-375" width="750" height="750" fill="#fff"/>
        <circle cx="-366" cy="-40" r="42" fill="#000"/>
        <circle cx="366" cy="-40" r="42" fill="#000"/>
        <circle cx="-240" cy="-282" r="42" fill="#000"/>
        <circle cx="240" cy="-282" r="42" fill="#000"/>
        <circle cx="-220" cy="298" r="42" fill="#000"/>
        <circle cx="220" cy="298" r="42" fill="#000"/>
      </mask>
      <radialGradient id="scene-tone" cx="55%" cy="45%" r="65%">
        <stop offset="0" stop-color="#e6a93a"/>
        <stop offset="0.55" stop-color="#7f7a35"/>
        <stop offset="1" stop-color="#0c3230"/>
      </radialGradient>
      <path id="brand-arc" d="M -250 0 A 250 250 0 0 1 250 0"/>
      <path id="country-arc" d="M -190 -40 A 200 200 0 0 1 190 -40"/>
      <path id="detail-arc" d="M -282 0 A 282 282 0 0 0 282 0"/>
    </defs>

    <g mask="url(#notch-mask)">
      <circle class="label-body" cx="0" cy="0" r="372"/>
      <circle class="border-band" cx="0" cy="0" r="343"/>
    </g>

    <circle class="name-ring" cx="0" cy="0" r="318"/>

    <circle class="scene-field" cx="0" cy="0" r="236" fill="url(#scene-tone)"
            role="img" aria-label="Engraved-style gold scene of a Riviera-like coastal village with palms, hills and a river"/>

    <text class="country" text-anchor="middle">
      <textPath href="#country-arc" startOffset="50%">NEW ZEALAND</textPath>
    </text>

    <text class="brand-name" text-anchor="middle">
      <textPath href="#brand-arc" startOffset="50%">DUNMORE HALE</textPath>
    </text>

    <text class="detail" text-anchor="middle">
      <textPath href="#detail-arc" startOffset="24%">SAUVIGNON BLANC</textPath>
    </text>
    <text class="detail" text-anchor="middle">
      <textPath href="#detail-arc" startOffset="76%">MARLBOROUGH</textPath>
    </text>

    <polygon class="star" transform="translate(0 268)"
      points="0,-15 4.4,-4.6 14.3,-4.6 6.2,2.0 9.3,12.1 0,6.0 -9.3,12.1 -6.2,2.0 -14.3,-4.6 -4.4,-4.6"/>
  </svg>
</main>
</body>
</html>
```